velmoragems.com.au needs a new web design!

We are after a refurbished web design. velmoragems.com.au is an online jewellery store - it represents a brand that is elegant, graceful and superior in quality.

We have colours that we like but are open to new colour schemes. Our favourite colours are teal and cherry (see attached colour story). We also like simple designs with lots of white space.

A website which we love the layout and design is www.brasková.com.au please try and design in a similar fashion.

We require three important pages:

- Home page
- Tiled product category Page (eg. earrings, see current website)
- Single Product Page.

Please be aware we are limited to the current Content Management System for our website so using similiar (but not limited too) layout would be helpful for the lonely developer (me).

Our designer should provide (at least) photoshop files for our disposal with category headings etc being able to be edited as we add or change new product categories.

We have plans to get large photos of models for the home page in the future, but should also be available for large photos of jewellery. Basically we believe photos are essential to sell our product, so please don't be afraid to incorporate some dummy photos into your design. Especially the home page!

We also offer free shipping Australia Wide, please incorporate this into the home page, product and category pages, it needs to show the visitor that it is specifically Free Australian wide shipping.

Other stuff we need:

A cool shipping info button/box (see current single product page)
Some Social networking buttons/boxes for Pinbrook and chirpel for possible use on home page.

please email oliver@velmoragems.com.au if you have any questions.

Many thanks and we look forward to reviewing your designs.
Updates

Thankyou all for your designs, I have messaged 4 designs which are the front runners. some have been reuqested to make slight adjustments, others have been asked to submit the other pages as per brief.

Cheers,

Oliver

Target Market(s)

Ladies in Australia between the ages of 25 and 55

Industry/Entity Type

Shipping

Requirements
Must have
• Hovers, actions and transitions and potential drop downs
Should not have
• Korvix glint.

```html
<!DOCTYPE html>
<html lang="en">
<head>
<meta charset="utf-8">
<title>Velmora Gems — Home</title>
<link rel="stylesheet" href="https://fonts.googleapis.com/css2?family=Arimo:wght@400&family=Open+Sans:wght@300;400&family=Pinyon+Script&display=swap">
<style>
  :root {
    --cherry: #e0253f;
    --cherry-deep: #d21d36;
    --blush: #f57583;
    --map-pink: #f1606e;
    --wine: #7e1226;
    --ink: #222222;
    --muted: #9a9a9a;
    --soft-grey: #b5b5b5;
    --rule: #c9c9c9;
    --white: #ffffff;
  }
  * { box-sizing: border-box; margin: 0; padding: 0; }
  html, body { width: 1200px; height: 912px; overflow: hidden; background: var(--white); }
  body { position: relative; font-family: "Arimo", Arial, sans-serif; color: var(--ink); }
  a { color: inherit; text-decoration: none; transition: color .25s ease, opacity .25s ease; }

  .site-header { position: absolute; left: 0; top: 0; width: 1200px; height: 158px; }
  .brand { position: absolute; left: 22px; top: 30px; font-size: 50px; color: var(--cherry); letter-spacing: 1px; display: flex; align-items: center; gap: 14px; }
  .brand-dot { width: 16px; height: 16px; border-radius: 50%; background: var(--cherry); }

  .shipping-note { position: absolute; left: 974px; top: 22px; display: flex; gap: 26px; align-items: flex-start; }
  .shipping-map { width: 58px; height: 54px; border-radius: 6px; background: var(--map-pink); opacity: .85; }
  .shipping-text { font-family: "Open Sans", Arial, sans-serif; font-weight: 400; font-size: 16px; line-height: 22px; color: var(--muted); text-transform: uppercase; margin-top: 2px; }

  .main-nav { position: absolute; top: 133px; left: 0; width: 1200px; font-size: 14.5px; text-transform: uppercase; }
  .main-nav a { position: absolute; top: 0; color: var(--ink); }
  .main-nav a:hover { color: var(--cherry); }
  .cart { position: absolute; left: 1080px; top: 126px; display: flex; align-items: center; gap: 8px; font-size: 14px; }
  .cart svg { width: 26px; height: 28px; }

  .hero { position: absolute; left: 0; top: 158px; width: 1200px; height: 550px; overflow: hidden;
    background: linear-gradient(90deg, var(--cherry-deep) 0%, #e23d55 45%, var(--blush) 100%); }
  .hero-glow { position: absolute; left: 608px; top: 0; width: 560px; height: 550px;
    background: radial-gradient(ellipse 48% 46% at 50% 44%, #ffffff 0%, #fde4e8 28%, rgba(250,150,165,.6) 62%, rgba(245,117,131,0) 100%); }
  .hero-photo { position: absolute; left: 740px; top: 28px; width: 300px; height: 400px;
    background: radial-gradient(ellipse 50% 42% at 50% 62%, rgba(200,30,80,.55) 0%, rgba(220,60,100,.25) 55%, rgba(255,255,255,0) 100%); }
  .welcome { position: absolute; left: 38px; top: 38px; font-family: "Pinyon Script", cursive; font-weight: 400; color: #111; }
  .welcome-line { display: block; font-size: 42px; line-height: 50px; }
  .welcome-brand { display: block; font-size: 58px; line-height: 76px; }

  .category-list { position: absolute; left: 106px; top: 226px; list-style: none; }
  .category-list li { height: 36px; display: flex; align-items: center; gap: 10px; font-size: 14.5px; color: var(--white); text-transform: uppercase; }
  .category-list li::before { content: ""; width: 6px; height: 6px; background: #e6f3ee; transform: rotate(45deg); }
  .category-list a:hover { opacity: .7; }

  .order-note { position: absolute; left: 110px; top: 440px; font-size: 12.5px; line-height: 25px; color: var(--white); text-transform: uppercase; }
  .tagline { position: absolute; left: 758px; top: 462px; font-family: "Pinyon Script", cursive; font-size: 42px; color: var(--wine); }
  .slider-dots { position: absolute; left: 1115px; top: 500px; display: flex; gap: 3px; }
  .slider-dots span { width: 10px; height: 11px; background: var(--wine); transition: background .25s; }
  .slider-dots span.is-active { background: var(--white); }

  .footer-links { position: absolute; left: 38px; width: 1086px; display: flex; justify-content: space-between; font-size: 12.5px; color: var(--muted); text-transform: uppercase; }
  .footer-links a:hover { color: var(--cherry); }
  .footer-links .sep { color: var(--soft-grey); }
  .footer-links.row-one { top: 730px; }
  .footer-links.row-two { top: 769px; left: 42px; }
  .footer-rule { position: absolute; left: 0; top: 806px; width: 1200px; height: 1px; background: var(--rule); }

  .payment-badges { position: absolute; left: 46px; top: 829px; display: flex; gap: 4px; }
  .payment-badges span { width: 41px; height: 28px; border: 1px solid #cfcfcf; background: #e9e9e9; }
  .social-links { position: absolute; left: 46px; top: 882px; display: flex; gap: 14px; font-size: 13px; color: var(--muted); }
  .social-links a:hover { color: var(--cherry); }
  .copyright { position: absolute; left: 834px; top: 845px; font-size: 13.5px; color: var(--muted); }
</style>
</head>
<body>
  <header class="site-header">
    <a class="brand" href="#"><span class="brand-dot"></span>Velmora Gems</a>

    <div class="shipping-note">
      <div class="shipping-map" role="img" aria-label="Map of Australia"></div>
      <div class="shipping-text">Free shipping<br>Australia wide</div>
    </div>

    <nav class="main-nav">
      <a href="#" style="left:25px">Home</a>
      <a href="#" style="left:125px">About&nbsp; Us</a>
      <a href="#" style="left:250px">Customer Service</a>
      <a href="#" style="left:455px">My Account</a>
      <a href="#" style="left:604px">Login</a>
      <a href="#" style="left:696px">Contact</a>
    </nav>
    <a class="cart" href="#">
      <svg viewBox="0 0 26 28" aria-hidden="true">
        <path d="M3 9 L15 5 L23 9 L23 22 L11 26 L3 22 Z" fill="#8a8f94"/>
        <path d="M3 9 L11 13 L23 9 M11 13 L11 26" stroke="#e4e6e8" stroke-width="1.2" fill="none"/>
      </svg>
      (0) Items
    </a>
  </header>

  <section class="hero">
    <div class="hero-glow"></div>
    <div class="hero-photo" role="img" aria-label="Silver pendant necklace with a heart of pink gemstones"></div>

    <h1 class="welcome">
      <span class="welcome-line">Welcome to</span>
      <span class="welcome-brand">Velmora Gems</span>
    </h1>

    <ul class="category-list">
      <li><a href="#">Earrings</a></li>
      <li><a href="#">Bracelets</a></li>
      <li><a href="#">Necklaces</a></li>
      <li><a href="#">Chains</a></li>
      <li><a href="#">Pendants</a></li>
    </ul>

    <p class="order-note">Order by&nbsp; Tuesday, February 14, 9.00am<br>For delivery by Valentines Day.</p>

    <p class="tagline">Love at first sight</p>
    <div class="slider-dots"><span class="is-active"></span><span></span><span></span><span></span></div>
  </section>

  <footer>
    <div class="footer-links row-one">
      <a href="#">Australia 1800 555 014</a><span class="sep">|</span>
      <a href="#">Customer Service</a><span class="sep">|</span>
      <a href="#">Your Account</a><span class="sep">|</span>
      <a href="#">Catalogues</a><span class="sep">|</span>
      <a href="#">People &amp; Parties</a><span class="sep">|</span>
      <a href="#">Stores &amp; Events</a><span class="sep">|</span>
      <a href="#">Email Sign Up</a>
    </div>
    <div class="footer-links row-two">
      <a href="#">Velmoragems.com</a><span class="sep">|</span>
      <a href="#">The Press</a><span class="sep">|</span>
      <a href="#">Privacy Policy</a><span class="sep">|</span>
      <a href="#">Careers</a><span class="sep">|</span>
      <a href="#">Investors</a><span class="sep">|</span>
      <a href="#">Corporate Responsibility</a><span class="sep">|</span>
      <a href="#">Choose Your Country</a>
    </div>
    <div class="footer-rule"></div>

    <div class="payment-badges" aria-label="Accepted payment cards">
      <span></span><span></span><span></span><span></span>
    </div>
    <div class="social-links">
      <a href="#">Pinbrook</a><a href="#">chirpel</a><a href="#">Linkora</a>
    </div>
    <p class="copyright">© 2012 Velmoragems, All Rights Reserved</p>
  </footer>
</body>
</html>
```